Wix Design for a Clothing Design Web Marketing Site

We need a Wix design and content (including any images and copy) for a clothing design web storefront, Lark & Loom (or larkandloom). Rough ideas and content can be found at http://marenholtvig.wix.com/larkandloom.

Lark and Loom is an innovative business concept that combines fashion and entertainment. The business model allows customers to actively participate in the creation of fashion designs/concepts , visualize the garment in the customer’s body in 3D, and buy the physical garment made specially to fit the customer.
The fashion consultant will be able to create the design based on client's desires and test various possibilities (size, fabric, cut, etc..) in front of the customer, using software Quendrax (the software is a key component of this business model)
(when developing the website use images from Quendrax)
After the design is created, the customer can choose to order the actual piece. The garment will be made according to the created design, the customer measurements.

Target Market(s)

Primarily women from 25 to 45, who are fashion enthusiasts and appreciate fit and exclusivity. They are hedonistic shoppers, who shop for entertainment.
Men (metrosexuals) who are fashion enthusiasts, also hedonistic shoppers.

Industry/Entity Type

Clothing

Font styles to use
Serif
Sans Serif

Requirements
Must have
• Must have a landing page (home) or section, that gives the consumer an idea of what Lark & Loom will do for them, an about page or section that tells about the company and product, a how it works page or section that describes how it works (http://marenholtvig.wix.com/larkandloom#!services3/c192y), and page or section about pricing, and a page or section on how to contact us.
Nice to have
• Very modern and clean. The website must be based on the main picture of the studio in the example. If that studio is the store, what will the website look like?
• Colors yellow, grey and white. Use the zig zag in yellow and white. You can change the size of the lines. The zig zagi gives the modern and bold accent. Outfits in pictures must show nicely tailored garments.

```html
<!DOCTYPE html>
<html lang="en">
<head>
<meta charset="utf-8">
<title>Lark and Loom — Clothes Made Specially</title>
<link rel="stylesheet" href="https://fonts.googleapis.com/css2?family=Raleway:wght@400;600;700&family=Oswald:wght@400;500&family=Lato:wght@300;700&family=Arimo:wght@400;700&display=swap">
<style>
:root{
  --yellow:#f2e600;
  --yellow-soft:#f7f08a;
  --yellow-pale:#fbf7c4;
  --ink:#1e1e1e;
  --bar:#222222;
  --white:#ffffff;
  --grey:#8a8a8a;
  --line:#cfcfcf;
  --price:#b3121b;
  --footer:#0b0b0b;
}
*{margin:0;padding:0;box-sizing:border-box}
html,body{width:1200px;height:2356px;overflow:hidden}
body{position:relative;font-family:"Arimo",Arial,sans-serif;color:var(--ink);background:var(--white)}
.abs{position:absolute}
.zigzag-field{position:absolute;left:0;width:1200px;background:linear-gradient(180deg,var(--yellow-pale),var(--yellow-soft) 50%,var(--yellow-pale))}

/* header */
.site-header{top:0;height:157px}
.brand{position:absolute;left:141px;top:107px;height:28px;padding:0 10px;background:var(--yellow);font-family:"Oswald",sans-serif;font-weight:500;font-size:19px;line-height:28px;color:var(--ink)}
.account-links{position:absolute;left:640px;top:20px;width:410px;display:flex;justify-content:space-between;font-size:12px;color:var(--ink)}
.promo-line{position:absolute;left:440px;top:97px;font-family:"Oswald",sans-serif;font-weight:500;font-size:16px;letter-spacing:.2px}
.cart{position:absolute;left:880px;top:84px;display:flex;gap:8px}
.cart-title{font-family:"Oswald",sans-serif;font-size:13px;font-weight:500;line-height:16px}
.cart-total{font-family:"Oswald",sans-serif;font-size:17px;line-height:20px}

/* nav */
.main-nav{left:0;top:157px;width:1200px;height:47px;background:var(--bar)}
.nav-item{position:absolute;top:0;line-height:47px;font-size:13px;color:var(--white);font-weight:400}
.nav-item.active{font-weight:700}
.nav-item.active::after{content:"";position:absolute;left:-12px;right:-12px;bottom:2px;height:3px;background:var(--yellow)}
.search{position:absolute;left:820px;top:166px;width:182px;height:29px;background:var(--white)}
.search-btn{position:absolute;left:1002px;top:166px;width:35px;height:29px;background:var(--yellow)}

/* hero */
.hero{left:0;top:204px;width:1200px;height:464px;background:linear-gradient(100deg,#5a1a10 0%,#b8321c 30%,#d24a22 55%,#8e2414 75%,#c2862e 100%)}
.hero-caption{position:absolute;left:286px;top:393px;width:619px;height:78px;background:rgba(242,230,0,.82);text-align:center}
.hero-title{font-family:"Raleway",sans-serif;font-weight:600;font-size:36px;letter-spacing:2px;line-height:50px;padding-top:4px}
.hero-sub{display:flex;align-items:center;justify-content:center;gap:10px;font-family:"Raleway",sans-serif;font-size:14px;letter-spacing:1px}
.hero-sub::before,.hero-sub::after{content:"";width:90px;height:1px;background:var(--ink)}
.dot{position:absolute;top:632px;width:18px;height:18px;border-radius:50%;background:var(--white)}
.dot.on{background:var(--yellow)}

/* promo tiles */
.tile{position:absolute;top:699px;width:286px;height:176px;border:4px solid var(--yellow)}
.tile-label{position:absolute;left:50%;transform:translateX(-50%);bottom:12px;background:var(--white);padding:2px 18px;font-family:"Lato",sans-serif;font-weight:300;font-size:29px;white-space:nowrap;line-height:40px}
.tile-label b{font-weight:700}

/* product grid */
.product-panel{left:138px;top:908px;width:924px;height:840px;background:var(--white)}
.product{position:absolute;width:205px}
.product-photo{height:253px}
.product-info{border:1px solid var(--line);height:110px;text-align:center;padding-top:12px}
.product-name{font-size:12px;line-height:18px;color:#333}
.stars{margin:6px 0 4px;letter-spacing:2px;font-size:10px;color:#aaa}
.price-old{font-size:13px;color:#333;text-decoration:line-through;margin-right:12px}
.price-new{font-size:13px;font-weight:700;color:var(--price)}

/* banner */
.shipping-banner{left:0;top:1775px;width:1200px;height:349px;background:linear-gradient(180deg,#3a3530,#27231f 60%,#1c1a17);text-align:center}
.banner-title{position:absolute;left:0;width:1200px;top:95px;font-family:"Raleway",sans-serif;font-weight:700;font-size:22px;color:var(--yellow)}
.banner-text{position:absolute;left:0;width:1200px;top:132px;font-family:"Raleway",sans-serif;font-size:18px;color:var(--white)}
.btn-continue{position:absolute;left:504px;top:198px;width:173px;height:45px;background:var(--yellow);font-size:12px;line-height:45px;color:var(--ink)}

/* footer */
.site-footer{left:0;top:2124px;width:1200px;height:193px;background:var(--footer);color:var(--white)}
.foot-col{position:absolute;top:28px}
.foot-head{font-family:"Oswald",sans-serif;font-size:14px;color:var(--yellow);display:flex;align-items:center;gap:8px;margin-bottom:10px}
.foot-link{font-size:12px;line-height:20.5px;color:#ddd}
.social{position:absolute;top:18px;width:38px;height:38px;border-radius:50%}
.social-rule{position:absolute;top:36px;height:1px;background:#444}
.news-title{position:absolute;left:713px;width:311px;top:80px;text-align:center;font-family:"Oswald",sans-serif;font-size:17px;color:var(--yellow)}
.news-sub{position:absolute;left:713px;width:311px;top:106px;text-align:center;font-size:12px;color:#bbb}
.news-input{position:absolute;left:713px;top:128px;width:267px;height:38px;background:var(--white);color:#999;font-size:12px;line-height:38px;padding-left:12px}
.news-btn{position:absolute;left:980px;top:128px;width:44px;height:38px;background:#5b3a6b}
.legal-bar{left:0;top:2317px;width:1200px;height:39px;background:var(--footer);border-top:1px solid #2a2a2a;color:#bbb;font-size:12px}
</style>
</head>
<body>

<div class="zigzag-field" role="img" aria-label="Yellow and white zigzag pattern background" style="top:0;height:157px"></div>
<header class="abs site-header" style="left:0;width:1200px">
  <div class="brand">Lark and Loom</div>
  <nav class="account-links"><span>My Account</span><span>|</span><span>My Wishlist</span><span>|</span><span>My Cart</span><span>|</span><span>Checkout</span><span>|</span><span>Log In</span></nav>
  <div class="promo-line">FREE SHIPPING ON ALL ORDERS. NO MINIMUM PURCHASE</div>
  <div class="cart">
    <svg width="42" height="40" viewBox="0 0 42 40" aria-hidden="true"><path d="M2 6h7l5 20h20l5-14H12" fill="none" stroke="#c0141b" stroke-width="3"/><circle cx="16" cy="33" r="3.5" fill="#c0141b"/><circle cx="31" cy="33" r="3.5" fill="#c0141b"/></svg>
    <div><div class="cart-title">SHOPPING CART</div><div class="cart-total">item(0) - $0.00</div></div>
  </div>
</header>

<nav class="abs main-nav">
  <span class="nav-item active" style="left:168px">HOME</span>
  <span class="nav-item" style="left:259px">WHAT IS LARK &amp; LOOM?</span>
  <span class="nav-item" style="left:454px">HOW IT WORKS</span>
  <span class="nav-item" style="left:608px">PRICE</span>
  <span class="nav-item" style="left:700px">CONTACT US</span>
</nav>
<div class="search"></div>
<div class="search-btn"><svg width="35" height="29" viewBox="0 0 35 29" aria-hidden="true"><circle cx="16" cy="13" r="6" fill="none" stroke="#1e1e1e" stroke-width="2.4"/><path d="M20.5 17.5l5 5" stroke="#1e1e1e" stroke-width="2.6"/></svg></div>

<section class="abs hero" role="img" aria-label="Model in a tailored striped dress posing beside a red carnival wagon and painted wheel">
</section>
<div class="hero-caption">
  <div class="hero-title">CLOTHES MADE SPECIALLY</div>
  <div class="hero-sub">FOR YOU AND DESIGNED BY YOU</div>
</div>
<span class="dot" style="left:973px"></span><span class="dot on" style="left:1001px"></span><span class="dot" style="left:1029px"></span>

<div class="zigzag-field" role="img" aria-label="Yellow and white zigzag pattern background" style="top:668px;height:1107px"></div>

<div class="tile" style="left:141px;background:linear-gradient(135deg,#f3efe9,#d9c6a8 60%,#8a5a4a)" role="img" aria-label="Woman with blonde hair carrying a patterned bag">
  <span class="tile-label"><b>20%</b> discount</span></div>
<div class="tile" style="left:459px;background:linear-gradient(90deg,#2c2420,#c2413a 50%,#7d7870)" role="img" aria-label="Woman in a red dress beside a stone wall">
  <span class="tile-label">star's wearing</span></div>
<div class="tile" style="left:774px;background:linear-gradient(135deg,#4a6a8a,#dcdcdc 50%,#2a2a2a)" role="img" aria-label="Person in jeans holding a black leather bag">
  <span class="tile-label">special <b>gift</b></span></div>

<section class="abs product-panel">
  <div class="product" style="left:14px;top:14px"><div class="product-photo" style="background:linear-gradient(180deg,#e8ecec,#d7e0e0)" role="img" aria-label="Model in a pink polo shirt and green trousers"></div><div class="product-info"><div class="product-name">Quam vitnibh aliqueobo egestas<br>lorem commodo</div><div class="stars">☆☆☆☆☆</div><span class="price-old">$23.99</span><span class="price-new">$18.99</span></div></div>
  <div class="product" style="left:248px;top:14px"><div class="product-photo" style="background:linear-gradient(180deg,#f0f0f0,#e6dfd6)" role="img" aria-label="Model in a camel coat and red trousers"></div><div class="product-info"><div class="product-name">Quam vitnibh aliqueobo egestas<br>lorem commodo</div><div class="stars">☆☆☆☆☆</div><span class="price-old">$23.99</span><span class="price-new">$18.99</span></div></div>
  <div class="product" style="left:478px;top:14px"><div class="product-photo" style="background:linear-gradient(180deg,#eeeeee,#dcd6d6)" role="img" aria-label="Model in a black vest over a red top"></div><div class="product-info" style="padding-top:16px"><div class="product-name">Quam vitnibh aliqueobo egestas<br>lorem commodo</div><div class="stars">☆☆☆☆☆</div><span class="price-old">$23.99</span><span class="price-new">$18.99</span></div></div>
  <div class="product" style="left:704px;top:14px"><div class="product-photo" style="background:linear-gradient(180deg,#f1f1f1,#dcdcdc)" role="img" aria-label="Model in a black leather jacket and trousers with a handbag"></div><div class="product-info" style="padding-top:16px"><div class="product-name">Quam vitnibh aliqueobo egestas<br>lorem commodo</div><div class="stars">☆☆☆☆☆</div><span class="price-old">$23.99</span><span class="price-new">$18.99</span></div></div>

  <div class="product" style="left:14px;top:415px"><div class="product-photo" style="background:linear-gradient(180deg,#f1f1f1,#dedede)" role="img" aria-label="Model in a printed knee-length dress"></div><div class="product-info"><div class="product-name">Quam vitnibh aliqueobo egestas<br>lorem commodo</div><div class="stars">☆☆☆☆☆</div><span class="price-old">$23.99</span><span class="price-new">$18.99</span></div></div>
  <div class="product" style="left:248px;top:415px"><div class="product-photo" style="background:linear-gradient(180deg,#f1f1f1,#dcd8d4)" role="img" aria-label="Model in a dark jacket and brown trousers with a bag"></div><div class="product-info"><div class="product-name">Quam vitnibh aliqueobo egestas<br>lorem commodo</div><div class="stars">☆☆☆☆☆</div><span class="price-old">$23.99</span><span class="price-new">$18.99</span></div></div>
  <div class="product" style="left:478px;top:415px"><div class="product-photo" style="background:linear-gradient(180deg,#f1f1f1,#e2d6d6)" role="img" aria-label="Model in a red duffle coat and grey hat"></div><div class="product-info"><div class="product-name">Quam vitnibh aliqueobo egestas<br>lorem commodo</div><div class="stars">☆☆☆☆☆</div><span class="price-old">$23.99</span><span class="price-new">$18.99</span></div></div>
  <div class="product" style="left:704px;top:415px"><div class="product-photo" style="background:linear-gradient(180deg,#f1f1f1,#dcdcdc)" role="img" aria-label="Model in a black leather jacket and trousers with a handbag"></div><div class="product-info"><div class="product-name">Quam vitnibh aliqueobo egestas<br>lorem commodo</div><div class="stars">☆☆☆☆☆</div><span class="price-old">$23.99</span><span class="price-new">$18.99</span></div></div>
</section>

<section class="abs shipping-banner" role="img" aria-label="Evening shopping street with pedestrians, darkened">
  <div class="banner-title">FREE SHIPPING ON ALL ORDERS ABOVE $200.00</div>
  <div class="banner-text">You have a total of $0.00 in your cart. Use another $200.00 to get free delivery!</div>
  <div class="btn-continue">CONTINUE SHOPPING »</div>
</section>

<footer class="abs site-footer">
  <div class="foot-col" style="left:166px">
    <div class="foot-head"><svg width="12" height="12" viewBox="0 0 12 12" aria-hidden="true"><path d="M1 1h5l5 5-5 5-5-5z" fill="#f2e600"/></svg>SHOP</div>
    <div class="foot-link">Upcoming Sales</div><div class="foot-link">Sales Ending Soon</div><div class="foot-link">Clothes Out</div><div class="foot-link">Accessories</div>
  </div>
  <div class="foot-col" style="left:355px">
    <div class="foot-head"><svg width="13" height="13" viewBox="0 0 13 13" aria-hidden="true"><circle cx="6.5" cy="6.5" r="6.5" fill="#f2e600"/><rect x="5.6" y="5" width="1.8" height="5" fill="#0b0b0b"/><rect x="5.6" y="2.6" width="1.8" height="1.6" fill="#0b0b0b"/></svg>ACTION &amp; INFO</div>
    <div class="foot-link">About Us</div><div class="foot-link">Press</div><div class="foot-link">Our Partners</div><div class="foot-link">Gift Certificates</div>
  </div>
  <div class="foot-col" style="left:531px">
    <div class="foot-head"><svg width="18" height="12" viewBox="0 0 18 12" aria-hidden="true"><circle cx="6" cy="3" r="3" fill="#f2e600"/><circle cx="13" cy="3.5" r="2.5" fill="#f2e600"/><path d="M0 12c0-4 3-6 6-6s6 2 6 6zM12 12c0-3 1-5 2-5s4 1 4 5z" fill="#f2e600"/></svg>CUSTOMER CARE</div>
    <div class="foot-link">Help / Customer Support</div><div class="foot-link">Return Policy</div><div class="foot-link">Shipping</div><div class="foot-link">FAQs</div>
  </div>
  <div class="social-rule" style="left:713px;width:32px"></div>
  <div class="social-rule" style="left:995px;width:29px"></div>
  <span class="social" style="left:751px;background:#3a3a46"></span>
  <span class="social" style="left:799px;background:#4a4a52"></span>
  <span class="social" style="left:848px;background:#5a5254"></span>
  <span class="social" style="left:898px;background:#44464e"></span>
  <span class="social" style="left:949px;background:#4e4446"></span>
  <div class="news-title">NEWSLETTER SIGNUP</div>
  <div class="news-sub">Preview sales, deals, news, updates, and more</div>
  <div class="news-input">Enter your email address...</div>
  <div class="news-btn"><svg width="44" height="38" viewBox="0 0 44 38" aria-hidden="true"><rect x="13" y="12" width="18" height="13" fill="none" stroke="#ffffff" stroke-width="1.6"/><path d="M13 12l9 7 9-7" fill="none" stroke="#ffffff" stroke-width="1.6"/></svg></div>
</footer>

<div class="abs legal-bar">
  <span class="abs" style="left:156px;top:12px">©&nbsp; 2015&nbsp; Lark and Loom&nbsp; |&nbsp; LLC. All Rights Reserved.</span>
  <span class="abs" style="left:780px;top:12px">Terms of us&nbsp; •&nbsp; Privacy Policy&nbsp; •&nbsp; Contact</span>
</div>

</body>
</html>
```